" 816 " PACKAGING FOR AUTOMOTIVE SPAREPARTS PRODUCT

We need a zipped plastic packaging design for our product (i attached plastic packaging sample from another product). The plastic size is 40cm (length) * 30cm (width) with zipped on upside.

Our product is rubber parts for car suspension application. The brand is 816 and the slogan is 816 ORIGINAL PARTS ( see attached file).

We prefer the design use mostly red color (same color as our logo) and combine with other attracting color and it is on your control.
I have included a picture of packaging box that we currently use.

On the front side of the plastic packaging should have a view window that can view and see through the product inside the packaging.

The color and the design is on your control.
Updates

Project Deadline Extended
Reason: Hi I extend the deadline, create your Best design..

Target Market(s)

All customers, car workshop, retailer and user.

Industry/Entity Type

Automotive

Requirements
Must have
• - A space for labeling on front side of the packaging. (label size 4cm (lenght) * 7cm (width).
• - Should have the Pictures of our product on the packaging. I have included some pictures of our product, You can choose and put some of the pictures on the packaging.
• - The design should can communicate HIGH QUALITY PARTS.
Nice to have
• - Have some Blue print or silhouette (with a bit transparancy) of car spareparts item or workshop tool kit on the design.

```html
<!DOCTYPE html>
<html lang="en">
<head>
<meta charset="utf-8">
<title>816 Packaging – Front and Back</title>
<link rel="stylesheet" href="https://fonts.googleapis.com/css2?family=Audiowide&family=Abel&family=Oswald:wght@600&family=Noto+Sans+JP:wght@300;400&family=Montserrat:wght@500&display=swap">
<style>
  :root {
    --red: #e31e25;
    --red-deep: #c01d2e;
    --white: #ffffff;
    --steel-dark: #3c3c3e;
    --steel-light: #d6d6d8;
    --canvas: #e4e4e4;
    --window-frame: #a7a9ac;
  }
  * { margin: 0; padding: 0; box-sizing: border-box; }
  html, body { width: 1200px; height: 900px; overflow: hidden; background: var(--canvas); }
  .stage { position: relative; width: 1200px; height: 900px; }
  .pack { position: absolute; top: 132px; width: 480px; height: 638px; overflow: hidden; }
  .pack--front { left: 92px; }
  .pack--back { left: 601px; }
  .pack svg { position: absolute; inset: 0; }
  .brand-name { font-family: "Audiowide", sans-serif; fill: var(--red); }
  .headline { font-family: "Audiowide", sans-serif; fill: var(--white); }
  .jp-tag { font-family: "Noto Sans JP", sans-serif; font-weight: 400; fill: var(--white); }
  .label-tab-text { font-family: "Oswald", sans-serif; font-weight: 600; fill: #1e1e1e; }

  .back-copy { position: absolute; left: 55px; right: 59px; top: 282px; color: var(--white); }
  .back-title { font-family: "Audiowide", sans-serif; font-style: italic; font-size: 28px; line-height: 28px; text-align: center; letter-spacing: 1px; }
  .back-title .jp { font-family: "Noto Sans JP", sans-serif; font-style: normal; font-size: 15px; letter-spacing: 0; margin-left: 6px; }
  .care-en { font-family: "Abel", sans-serif; font-size: 12.5px; line-height: 15.6px; margin-top: 10px; }
  .care-en .line { display: block; }
  .care-en .line--full { text-align: justify; text-align-last: justify; }
  .care-jp { font-family: "Noto Sans JP", sans-serif; font-weight: 300; font-size: 13.5px; line-height: 15.6px; margin-top: 14px; white-space: nowrap; }
  .slogan-jp { font-family: "Noto Sans JP", sans-serif; font-weight: 300; font-size: 13px; margin-top: 16px; }
  .sign-off { font-family: "Abel", sans-serif; font-size: 13.5px; line-height: 16px; margin-top: 14px; }
  .sign-off strong { font-family: "Oswald", sans-serif; font-weight: 600; font-size: 13px; letter-spacing: .3px; }
  .origin { position: absolute; left: 0; right: 0; top: 602px; text-align: center; color: var(--white); font-family: "Montserrat", sans-serif; font-weight: 500; font-size: 12.5px; letter-spacing: .5px; }
</style>
</head>
<body>
<div class="stage">

  <section class="pack pack--front" aria-label="Front of package">
    <svg width="480" height="638" viewBox="0 0 480 638">
      <defs>
        <linearGradient id="steel-front" x1="0" y1="1" x2="1" y2="0">
          <stop offset="0" stop-color="var(--steel-dark)"/>
          <stop offset=".45" stop-color="var(--steel-light)"/>
          <stop offset="1" stop-color="var(--steel-dark)"/>
        </linearGradient>
        <linearGradient id="tab-steel" x1="0" y1="0" x2="1" y2="0">
          <stop offset="0" stop-color="#6d6e71"/>
          <stop offset=".5" stop-color="#e6e7e8"/>
          <stop offset="1" stop-color="#6d6e71"/>
        </linearGradient>
      </defs>
      <rect class="pack-base" width="480" height="638" fill="var(--white)"/>
      <polygon class="steel-band" points="0,240 460,0 480,0 480,10 0,290" fill="url(#steel-front)"/>
      <polygon class="red-band" points="0,284 480,0 480,638 0,638" fill="var(--red)"/>
      <polygon class="red-deep-field" points="0,402 480,84 480,638 0,638" fill="var(--red-deep)"/>
      <rect class="lower-field" x="0" y="408" width="480" height="230" fill="var(--red-deep)" role="img" aria-label="Faint circuit-line pattern area"/>

      <text class="brand-name" x="60" y="140" font-size="68">816</text>

      <g transform="translate(44 312) rotate(-32)">
        <text class="headline" x="0" y="0" font-size="40" textLength="412" lengthAdjust="spacingAndGlyphs" transform="skewX(-12)">HIGH QUALITY</text>
      </g>
      <g transform="translate(16 376) rotate(-32)">
        <text class="headline" x="0" y="0" font-size="40" textLength="316" lengthAdjust="spacingAndGlyphs" transform="skewX(-12)">AUTO PARTS</text>
        <text class="jp-tag" x="334" y="-4" font-size="19" textLength="178" lengthAdjust="spacingAndGlyphs">高品質の自動車部品</text>
      </g>

      <path class="view-window" d="M72,430 Q68,418 80,410 L424,212 Q434,206 434,218 L434,570 Q434,582 422,582 L80,582 Q68,582 68,570 Z"
            fill="var(--white)" stroke="var(--window-frame)" stroke-width="6"/>

      <path class="label-tab" d="M126,585 L354,585 L346,614 Q342,626 330,626 L150,626 Q138,626 134,614 Z" fill="url(#tab-steel)"/>
      <text class="label-tab-text" x="240" y="616" font-size="22" text-anchor="middle">816 ORIGINAL PART</text>
    </svg>
  </section>

  <section class="pack pack--back" aria-label="Back of package">
    <svg width="480" height="638" viewBox="0 0 480 638">
      <defs>
        <linearGradient id="steel-back" x1="0" y1="1" x2="1" y2="0">
          <stop offset="0" stop-color="var(--steel-dark)"/>
          <stop offset=".45" stop-color="var(--steel-light)"/>
          <stop offset="1" stop-color="var(--steel-dark)"/>
        </linearGradient>
      </defs>
      <rect width="480" height="638" fill="var(--white)"/>
      <polygon class="steel-band" points="0,244 462,0 480,0 480,10 0,290" fill="url(#steel-back)"/>
      <polygon class="red-band" points="0,284 480,0 480,638 0,638" fill="var(--red)"/>
      <polygon class="red-deep-field" points="0,404 481,124 481,638 0,638" fill="var(--red-deep)"/>
      <text class="brand-name" x="60" y="140" font-size="68">816</text>
    </svg>

    <div class="back-copy">
      <h1 class="back-title">HIGH QUALITY<br>AUTO PARTS<span class="jp">高品質の自動車部品</span></h1>
      <p class="care-en">
        <span class="line">This product must be Properly Installed to prolong expected performance.</span>
        <span class="line line--full">Before Installation, consult manufacture's maintenance manual for</span>
        <span class="line">instruction to prevent premature failure of this product.</span>
      </p>
      <p class="care-jp">本製品は期待された性能を維持するために正しくインストール<br>する必要が有ります。<br>インストールする前に、本製品の早期故障を防止するため製造<br>元の保守マニュアルを参照してください。</p>
      <p class="slogan-jp">”高品質オートパーツ”</p>
      <p class="sign-off"><strong>HIGH QUALITY AUTO PARTS</strong><br>816 Original Parts</p>
    </div>
    <p class="origin">MADE IN INDONESIA</p>
  </section>

</div>
</body>
</html>
```